Lantern Holdings Business Card

We are looking to design new business cards for our company. We have two office locations and would like to have both full addresses on the card. Each address needs two lines for the building name and street address and a line or two for the city, state and zip code. There should be a place for 2-3 phone numbers. The addresses and phone numbers are at the bottom of this description. We also need a place to put our company website and one email address. Our logo is attached.
We would like the card to be two sided. The back of the card should have a blue background with some part of our logo design on it. We would like the full logo on the front of the card as well. The front of the card should have a white background with the blue logo. We are open to listing our addresses on the front or the back of the card. The person who designed our logo gave us an excellent business card idea that we really liked. I have attached a picture of his business card idea so that we can build off of it.
Addresses:
The Marlow Exchange
2214 47th Street NW
Washington, DC 20419
Osprey Harbor Tower
815 Tamsin Boulevard #2207
Miami, FL 33987
Phone Numbers: (202) 555-0148
(202) 555-0193
Website: www.lanternholdings-example.com

```html
<!DOCTYPE html>
<html lang="en">
<head>
<meta charset="utf-8">
<title>Lantern Holdings Business Card</title>
<link rel="stylesheet" href="https://fonts.googleapis.com/css2?family=Source+Sans+3:wght@400&display=swap">
<style>
  :root {
    --navy: #2a347a;
    --lavender: #a9aed1;
    --white: #ffffff;
    --backdrop: #e8e5e0;
  }
  * { box-sizing: border-box; margin: 0; padding: 0; }
  html, body {
    width: 1200px;
    height: 1000px;
    overflow: hidden;
    background: var(--backdrop);
    font-family: "Source Sans 3", sans-serif;
    font-weight: 400;
  }
  .canvas {
    position: relative;
    width: 1200px;
    height: 1000px;
  }
  .card {
    position: absolute;
    left: 200px;
    width: 800px;
    height: 457px;
    border-radius: 34px;
    overflow: hidden;
    box-shadow: 0 6px 18px rgba(0, 0, 0, 0.18);
  }
  /* Front */
  .card-front {
    top: 28px;
    background: var(--white);
  }
  .front-brand {
    position: absolute;
    left: 150px;
    top: 150px;
    display: flex;
    align-items: center;
    gap: 26px;
    color: var(--navy);
  }
  .brand-square {
    width: 108px;
    height: 108px;
    background: var(--navy);
    border-radius: 12px;
  }
  .front-name {
    font-size: 70px;
    letter-spacing: 1px;
    line-height: 1;
  }
  .front-band {
    position: absolute;
    left: 0;
    bottom: 0;
    width: 100%;
    height: 64px;
    background: var(--navy);
    color: var(--white);
    display: flex;
    align-items: center;
    justify-content: center;
    font-size: 26px;
  }
  /* Back */
  .card-back {
    top: 515px;
    background: var(--navy);
    color: var(--white);
  }
  .back-name {
    position: absolute;
    left: 52px;
    top: 28px;
    font-size: 52px;
    letter-spacing: 1px;
    line-height: 1;
  }
  .addresses {
    position: absolute;
    left: 56px;
    top: 100px;
    font-size: 26px;
    line-height: 1.18;
  }
  .address-block + .address-block { margin-top: 12px; }
  .contact {
    position: absolute;
    left: 44px;
    bottom: 30px;
    display: flex;
    flex-direction: column;
    gap: 8px;
    font-size: 26px;
    line-height: 1.2;
  }
  .phones {
    display: flex;
    gap: 44px;
  }
  .contact-item {
    display: flex;
    align-items: center;
    gap: 8px;
  }
  .icon-phone { width: 14px; height: 22px; }
  .icon-mail { width: 22px; height: 16px; }
  .back-mark {
    position: absolute;
    right: -40px;
    bottom: -40px;
    width: 260px;
    height: 260px;
    background: var(--lavender);
  }
</style>
</head>
<body>
<main class="canvas">
  <section class="card card-front" aria-label="Card front">
    <div class="front-brand">
      <span class="brand-square" aria-hidden="true"></span>
      <span class="front-name">Lantern Holdings</span>
    </div>
    <div class="front-band">www.lanternholdings-example.com</div>
  </section>

  <section class="card card-back" aria-label="Card back">
    <div class="back-name">Lantern Holdings</div>
    <div class="addresses">
      <p>Addresses:</p>
      <div class="address-block">
        <p>The Marlow Exchange</p>
        <p>2214 47th Street NW</p>
        <p>Washington, DC 20419</p>
      </div>
      <div class="address-block">
        <p>Osprey Harbor Tower</p>
        <p>815 Tamsin Boulevard #2207</p>
        <p>Miami, FL 33987</p>
      </div>
    </div>
    <div class="contact">
      <span class="contact-item email">
        <svg class="icon-mail" viewBox="0 0 22 16" aria-hidden="true"><rect x="1" y="1" width="20" height="14" rx="2" fill="none" stroke="#ffffff" stroke-width="2"/><path d="M2 2 L11 9 L20 2" fill="none" stroke="#ffffff" stroke-width="2"/></svg>
        info@lanternholdings-example.com
      </span>
      <div class="phones">
        <span class="contact-item phone">
          <svg class="icon-phone" viewBox="0 0 14 22" aria-hidden="true"><rect x="1" y="1" width="12" height="20" rx="2" fill="none" stroke="#ffffff" stroke-width="2"/><rect x="4" y="16" width="6" height="2" fill="#ffffff"/></svg>
          (202) 555-0148
        </span>
        <span class="contact-item phone">
          <svg class="icon-phone" viewBox="0 0 14 22" aria-hidden="true"><rect x="1" y="1" width="12" height="20" rx="2" fill="none" stroke="#ffffff" stroke-width="2"/><rect x="4" y="16" width="6" height="2" fill="#ffffff"/></svg>
          (202) 555-0193
        </span>
      </div>
    </div>
    <div class="back-mark" aria-hidden="true"></div>
  </section>
</main>
</body>
</html>
```